Virtual Reality company needs business card design

We would like a business card that is simple and memorable. Telvani is a global startup based in San Francisco and Singapore. We are a company with products and services for both the B2B and B2C audiences. We develop platforms with educational content, and allow people to interact with the content in a virtual environment setting. Our end user will be able to learn and 'see' the world's culture and history from the comfort of their home. The business card will primarily be used for B2B audience and not overly corporate in image, but requires a universal appeal - evoking sense of friendliness and innovation. Attached is our logo with two color options. We are open to single-sided or double-sided designs. EPS/AI files will be provided to winning designer at final design stage.

Other text that will be included in card: (Name), (Address), (Tel), (Email), (Website)

Include option of having TWO QR codes which are 0.5 inch x 0.5 inch each
Updates

Dear Designers,

Thank you for your submissions. We are currently in process of reviewing your designs and will make a decision in the next few days.

Regards,
Telvani

Industry/Entity Type

Environment

Font styles to use
Serif
Sans Serif

Requirements
Must have
• Spacing for Name, Address, Tel, Email, Web address
Should not have
• Limit the number of colors utilised.

```html
<!DOCTYPE html>
<html lang="en">
<head>
<meta charset="utf-8">
<title>Telvani Business Card</title>
<link href="https://fonts.googleapis.com/css2?family=Open+Sans:wght@400;600;700&display=swap" rel="stylesheet">
<style>
  :root {
    --brand-blue: #3399d6;
    --ink: #2b2b2b;
    --muted-ink: #555555;
    --card-white: #ffffff;
    --backdrop: #e9e9e9;
    --card-edge: #444444;
    --divider: #8a8a8a;
  }
  html, body {
    margin: 0;
    padding: 0;
    overflow: hidden;
  }
  body {
    width: 1200px;
    height: 1185px;
    background: var(--backdrop);
    position: relative;
    font-family: "Open Sans", sans-serif;
    color: var(--ink);
  }
  .card {
    position: absolute;
    background: var(--card-white);
    border: 1px solid var(--card-edge);
    overflow: hidden;
    box-sizing: border-box;
  }
  .card--front { left: 34px; top: 34px; width: 938px; height: 537px; }
  .card--back { left: 224px; top: 613px; width: 937px; height: 536px; }

  .corner-peel {
    position: absolute;
    left: 0; top: 0;
    width: 100%; height: 100%;
  }
  .holder {
    position: absolute;
    right: 24px;
    top: 30px;
    text-align: right;
    color: var(--card-white);
  }
  .holder__name { font-weight: 700; font-size: 29px; line-height: 1.2; }
  .holder__title { font-weight: 400; font-size: 21px; line-height: 1.3; }

  .wordmark {
    position: absolute;
    color: var(--brand-blue);
    font-weight: 400;
    line-height: 1;
    white-space: nowrap;
  }
  .card--front .wordmark { left: 40px; top: 92px; font-size: 124px; letter-spacing: 1px; }
  .card--back .wordmark { left: 0; right: 0; text-align: center; top: 126px; font-size: 142px; letter-spacing: 1px; }

  .contact-list {
    position: absolute;
    left: 42px;
    top: 360px;
    margin: 0;
    padding: 0;
    list-style: none;
    font-size: 22px;
    line-height: 36.5px;
  }
  .contact-list li { display: flex; align-items: center; gap: 8px; }
  .contact-icon { width: 18px; height: 18px; flex: none; }

  .divider {
    position: absolute;
    left: 351px;
    top: 422px;
    width: 1px;
    height: 86px;
    background: var(--divider);
  }
  .address {
    position: absolute;
    left: 372px;
    top: 432px;
    font-size: 22px;
    line-height: 37px;
    font-style: normal;
  }
  .website {
    position: absolute;
    left: 0; right: 0;
    top: 400px;
    text-align: center;
    font-size: 28px;
    letter-spacing: 3px;
    color: var(--muted-ink);
  }
</style>
</head>
<body>

<section class="card card--front">
  <svg class="corner-peel" viewBox="0 0 627 359" preserveAspectRatio="none" aria-hidden="true">
    <defs>
      <linearGradient id="curlShade" x1="0.2" y1="0" x2="0.9" y2="1">
        <stop offset="0" stop-color="#3a3a3a"/>
        <stop offset="0.55" stop-color="#7d7d7d"/>
        <stop offset="1" stop-color="#f2f2f2"/>
      </linearGradient>
    </defs>
    <polygon points="289,0 627,0 627,134" fill="var(--brand-blue)"/>
    <path d="M289,0 L627,134 Q586,150 574,225 Q500,110 289,0 Z" fill="url(#curlShade)"/>
  </svg>

  <div class="holder">
    <div class="holder__name">Your Name</div>
    <div class="holder__title">Title</div>
  </div>

  <div class="wordmark">Telvani</div>

  <ul class="contact-list">
    <li>
      <svg class="contact-icon" viewBox="0 0 16 16" aria-hidden="true"><circle cx="8" cy="8" r="7" fill="none" stroke="#2b2b2b" stroke-width="1.3"/><path d="M5.5 4.5 Q4.5 8 8 11.5 L9.5 10 L8.3 8.8 L7.6 9.3 Q6.5 8 6.8 6.7 L7.5 6.3 L6.8 4.8 Z" fill="#2b2b2b"/></svg>
      014-555-0192
    </li>
    <li>
      <svg class="contact-icon" viewBox="0 0 16 16" aria-hidden="true"><rect x="4.5" y="3" width="7" height="12" rx="1" fill="#2b2b2b"/><rect x="5.8" y="4.5" width="4.4" height="3.5" fill="#fff"/><rect x="9" y="0.5" width="1.2" height="3" fill="#2b2b2b"/></svg>
      014-555-0192
    </li>
    <li>
      <svg class="contact-icon" viewBox="0 0 16 16" aria-hidden="true"><path d="M1.5 6.5 L8 2.5 L14.5 6.5 V13.5 H1.5 Z" fill="#2b2b2b"/><path d="M3 7 L8 10 L13 7" fill="none" stroke="#fff" stroke-width="1.2"/></svg>
      hello@telvani.com
    </li>
    <li>
      <svg class="contact-icon" viewBox="0 0 16 16" aria-hidden="true"><g fill="none" stroke="#2b2b2b" stroke-width="1.2"><circle cx="8" cy="8" r="6.5"/><ellipse cx="8" cy="8" rx="3" ry="6.5"/><path d="M1.5 8 H14.5 M2.5 4.8 H13.5 M2.5 11.2 H13.5"/></g></svg>
      www.telvanivr.com
    </li>
  </ul>

  <div class="divider"></div>

  <address class="address">
    Street Name, City Name<br>
    Zip Code-00000
  </address>
</section>

<section class="card card--back">
  <div class="wordmark">Telvani</div>
  <div class="website">www.telvanivr.com</div>
</section>

</body>
</html>
```